New Product/Company Launch Postcard Design

I need a postcard design for a new product launch/new company called Trinvelas. Trinvelas are decorative ring hooks designed to decorate home fixtures for holidays, seasons and special occasions. The rings have hooks for hanging your favorite hanging ornaments, party decorations or fashionable accessories. Trinvelas comes in 3 sizes; small, medium and large with 4 available colors to accommodate most home fixtures. The rings have a split opening for easy attaching or placing on home fixtures, so there are no tools, no glue, the ring is easily attachable. The rings are simply easy to decorate and easy to create ideas.

I would like the postcard to communicate the product use and would like it to drive customers to my website. On this postcard, I am offering $4.99 2-pack special, Introductory offer. I would also like the postcard to direct them to my website to sign up for specials and offers, by doing so, I will give away a free small Trinvela. Please visit my website at www.trinvelasdesigns.com for other creative ideas.

I had someone create the logo, the colors I chose were black, hot pink and yellow. However, if the logo doesn't seem to work on the design, I am open for comments or other ideas.

```html
<!DOCTYPE html>
<html lang="en">
<head>
<meta charset="utf-8">
<title>Trinvelas Launch Postcard</title>
<link href="https://fonts.googleapis.com/css2?family=Lato:wght@400;700;900&family=Oswald:wght@500&display=swap" rel="stylesheet">
<style>
  :root {
    --hot-pink: #e5237f;
    --ink: #111111;
    --paper: #ffffff;
    --stage: #d9d9dc;
    --text-dark: #222222;
    --line-grey: #888888;
  }
  * { box-sizing: border-box; margin: 0; padding: 0; }
  html, body { width: 822px; height: 1200px; overflow: hidden; }
  body {
    background: var(--stage);
    font-family: "Lato", Arial, sans-serif;
    position: relative;
  }
  .card {
    position: absolute;
    left: 71px;
    width: 680px;
    height: 520px;
    overflow: hidden;
    box-shadow: 0 3px 10px rgba(0,0,0,.25);
  }
  .card-front { top: 50px; }
  .card-back { top: 625px; background: var(--paper); }
  .card-shape { position: absolute; inset: 0; }

  /* Front */
  .photo { position: absolute; }
  .photo-vase {
    left: 14px; top: 30px; width: 110px; height: 250px;
    border-radius: 40% 40% 30% 30%;
    background: linear-gradient(180deg, #6e5a3a, #8c7450 50%, #4a3b25);
  }
  .photo-pendants {
    left: 140px; top: 24px; width: 330px; height: 145px;
    border-radius: 6px;
    background: linear-gradient(90deg, #c9c2b3, #e9e6df 40%, #c6dbe5 65%, #a9c48f);
  }
  .photo-circle {
    border-radius: 50%;
    border: 9px solid var(--ink);
    box-shadow: 0 0 0 3px var(--paper);
  }
  .photo-lamp-a { left: 142px; top: 243px; width: 120px; height: 120px; background: radial-gradient(circle at 50% 40%, #e8d3a2, #7a5a32 75%); }
  .photo-lamp-b { left: 320px; top: 249px; width: 120px; height: 120px; background: radial-gradient(circle at 50% 35%, #f2e2bd, #6b4a2c 75%); }
  .photo-sconce { left: 507px; top: 197px; width: 130px; height: 130px; background: radial-gradient(circle at 50% 45%, #e7c27c, #5a3a1f 75%); }

  .brand-box {
    position: absolute; left: 491px; top: 30px; width: 148px; height: 64px;
    background: var(--hot-pink);
    border: 3px solid var(--ink);
    border-radius: 12px;
    display: flex; align-items: center; justify-content: center; gap: 8px;
  }
  .brand-name { font-weight: 900; font-size: 26px; color: #ffe600; letter-spacing: .3px; }
  .brand-dot { width: 12px; height: 12px; border-radius: 50%; background: #ffe600; }

  .headline {
    position: absolute; left: 296px; top: 178px; width: 215px;
    font-weight: 900; font-size: 12.5px; line-height: 1.3; text-transform: uppercase;
  }
  .headline .accent { color: var(--hot-pink); display: block; }
  .headline .rest { color: var(--text-dark); display: block; }

  .tagline-pill {
    position: absolute; left: 0; top: 368px; width: 355px; height: 40px;
    background: var(--paper);
    border-radius: 0 22px 22px 0;
    display: flex; align-items: center; padding-left: 18px;
    font-weight: 700; font-size: 17px; color: var(--ink);
  }
  .benefit-list {
    position: absolute; left: 16px; top: 424px; right: 20px;
    list-style: none; color: var(--paper); font-size: 10px; line-height: 1.55;
  }
  .benefit-list li { padding-left: 14px; position: relative; }
  .benefit-list li::before {
    content: ""; position: absolute; left: 0; top: 4px;
    width: 7px; height: 7px; background: var(--paper); border-radius: 50%;
  }

  /* Back */
  .info-pill {
    position: absolute; left: 0; height: 42px;
    background: var(--paper);
    border-radius: 0 22px 22px 0;
    display: flex; align-items: center; padding-left: 18px;
    font-weight: 700; font-size: 13.5px; color: var(--ink);
  }
  .pill-sizes { top: 26px; width: 285px; }
  .pill-colors { top: 240px; width: 182px; }
  .pill-uses { top: 336px; width: 182px; }
  .info-text {
    position: absolute; left: 18px; color: var(--paper);
    font-size: 16px; line-height: 1.22;
  }
  .sizes-text { top: 84px; width: 275px; }
  .colors-text { top: 298px; font-size: 15px; white-space: nowrap; }
  .use-list {
    position: absolute; left: 18px; top: 398px; list-style: none;
    color: var(--paper); font-size: 15px; line-height: 1.5; white-space: nowrap;
  }
  .use-list li { padding-left: 20px; position: relative; }
  .use-list li::before {
    content: ""; position: absolute; left: 2px; top: 7px;
    width: 10px; height: 10px; background: var(--paper); border-radius: 50%;
  }

  .stamp-box { position: absolute; left: 545px; top: 51px; width: 92px; height: 87px; border: 1.5px solid var(--ink); }
  .address-line { position: absolute; left: 402px; width: 258px; height: 1px; background: var(--line-grey); }
  .line-1 { top: 184px; } .line-2 { top: 228px; } .line-3 { top: 271px; }

  .blurb {
    position: absolute; right: 18px; top: 322px; width: 250px;
    text-align: right; font-size: 16px; line-height: 1.25; color: var(--ink);
  }
  .contact-row { position: absolute; left: 400px; display: flex; align-items: center; gap: 10px; }
  .row-phone { top: 400px; }
  .row-web { top: 448px; }
  .contact-icon { width: 30px; height: 30px; flex: none; }
  .phone-number { font-family: "Oswald", "Arial Narrow", sans-serif; font-weight: 500; font-size: 36px; color: var(--hot-pink); letter-spacing: 1px; line-height: 1; }
  .web-address { font-weight: 700; font-size: 17px; color: var(--ink); white-space: nowrap; }
</style>
</head>
<body>

<section class="card card-front">
  <svg class="card-shape" viewBox="0 0 680 520" aria-hidden="true">
    <rect width="680" height="520" fill="var(--hot-pink)"/>
    <path d="M0,22 H680 V178 C580,190 470,226 360,262 C240,300 120,306 0,292 Z" fill="var(--paper)"/>
    <path d="M0,300 C120,314 240,308 360,270 C470,234 580,198 680,186" fill="none" stroke="var(--ink)" stroke-width="7"/>
  </svg>

  <div class="photo photo-vase" role="img" aria-label="Bronze beaded vase decorated with hanging rings"></div>
  <div class="photo photo-pendants" role="img" aria-label="Pendant lights with hanging decorations attached"></div>

  <div class="brand-box"><span class="brand-dot"></span><span class="brand-name">Trinvelas</span></div>

  <p class="headline">
    <span class="accent">A "New" simple solution hook</span>
    <span class="rest">for hanging decorative accessories</span>
  </p>

  <div class="photo photo-circle photo-lamp-a" role="img" aria-label="Table lamp decorated with a ring"></div>
  <div class="photo photo-circle photo-lamp-b" role="img" aria-label="Shaded lamp in a living room"></div>
  <div class="photo photo-circle photo-sconce" role="img" aria-label="Candle holder with hanging accessory"></div>

  <div class="tagline-pill">Impress your Home - with Trinvelas</div>

  <ul class="benefit-list">
    <li>Accessorize your light fixtures and home fixtures with Trinvelas, a simplifying solution ring hook for creative decorating..</li>
    <li>Available in a selection of oil bronze, black, white and nickel silver. Our Trinvelas will blend in easily with your existing Decor.</li>
    <li>Use your own creativity and create unique designs with all your home fixtures.</li>
    <li>Use Trinvelas for Themed Party Decorations, Special Occasion Decorations, Holiday and Seasonal Hanging Decorations.</li>
  </ul>
</section>

<section class="card card-back">
  <svg class="card-shape" viewBox="0 0 680 520" aria-hidden="true">
    <path d="M0,0 H340 C312,140 310,320 350,430 C362,470 375,500 390,520 H0 Z" fill="var(--hot-pink)"/>
    <path d="M350,0 C322,140 320,320 360,430 C372,470 385,500 400,520" fill="none" stroke="var(--ink)" stroke-width="7"/>
  </svg>

  <div class="info-pill pill-sizes">Trinvelas comes in 3 different sizes:</div>
  <p class="info-text sizes-text">
    Small (58mm) Ideal for vases and smaller candle sticks<br>
    Medium (70mm) Ideal for pendant lights and table lamps<br>
    Large (96mm) Ideal for larger candle holders and dining chandeliers
  </p>

  <div class="info-pill pill-colors">Available in 4 colors:</div>
  <p class="info-text colors-text">Oil Bronze, White, Nickel Silver and Black</p>

  <div class="info-pill pill-uses">Use Trinvelas for:</div>
  <ul class="use-list">
    <li>Themed Party Hanging Decorations</li>
    <li>Special Occasion Hanging Decorations</li>
    <li>Holiday and Seasonal Hanging Decoration</li>
    <li>Fashionable Hanging Accessories</li>
  </ul>

  <div class="stamp-box"></div>
  <div class="address-line line-1"></div>
  <div class="address-line line-2"></div>
  <div class="address-line line-3"></div>

  <p class="blurb">Lorem Ipsum is simply dummy text of the printing and typesetting industry.</p>

  <div class="contact-row row-phone">
    <svg class="contact-icon" viewBox="0 0 34 34" aria-hidden="true">
      <rect width="34" height="34" rx="5" fill="var(--ink)"/>
      <path d="M12 7 C9 8 8 11 9 15 C11 21 15 25 20 27 C23 28 26 27 27 24 L23 20 L20 22 C17 20 14 17 13 14 L15 11 Z" fill="var(--paper)"/>
    </svg>
    <span class="phone-number">000-000-000</span>
  </div>
  <div class="contact-row row-web">
    <svg class="contact-icon" viewBox="0 0 34 34" aria-hidden="true">
      <rect x="4" y="9" width="26" height="17" fill="var(--ink)"/>
      <path d="M4 9 L17 19 L30 9" fill="none" stroke="var(--paper)" stroke-width="2"/>
    </svg>
    <span class="web-address">www.trinvelasdesigns.com</span>
  </div>
</section>

</body>
</html>
```